Female Pest Controller needs awesome business cards

I need a logo design for a Pest Control service - something that appeals to 'nature' & safe, with the use of the colour green. I am also female
New Business Name is 'Bug Begone Bay'
appeals to women

Target Market(s)

Domestic Households & Local Businesses

Industry/Entity Type

Pest Control

Contact Information for Business Card

Corinne Waldrake
0428316952
ABN 47 618 259 304
PMT7314958207
Spiders Cockroaches, Ants, Silverfish, Fleas, Rodents

Font styles to use
Decorative

Colors
abd036
aaaaaa
5c5c5c

Requirements
Should not have
• Pics of dead insects, prefer nature inspired designs, frogs, trees etc
• Have attached old log & business name ( now my ex's business) Lilyvale Pest Solutions -

```html
<!DOCTYPE html>
<html lang="en">
<head>
<meta charset="utf-8">
<title>Bug Begone Bay – Business Card</title>
<link href="https://fonts.googleapis.com/css2?family=Montserrat:wght@500;600;700&family=Questrial&display=swap" rel="stylesheet">
<style>
  :root {
    --leaf-green: #abd036;
    --charcoal: #5c5c5c;
    --white: #ffffff;
    --backdrop: #ebe8e4;
  }
  * { margin: 0; padding: 0; box-sizing: border-box; }
  html, body {
    width: 1200px;
    height: 1000px;
    overflow: hidden;
    background: var(--backdrop);
  }
  .canvas {
    position: relative;
    width: 1200px;
    height: 1000px;
  }
  .card {
    position: absolute;
    top: 0;
    width: 600px;
    height: 368px;
    color: var(--white);
    text-align: center;
  }
  .card--front {
    left: 0;
    background: var(--leaf-green);
  }
  .card--back {
    left: 600px;
    background: var(--charcoal);
  }

  /* Front */
  .brand {
    position: absolute;
    left: 0;
    right: 0;
    top: 150px;
    display: flex;
    align-items: center;
    justify-content: center;
    gap: 14px;
  }
  .brand__dot {
    width: 18px;
    height: 18px;
    border-radius: 50%;
    background: var(--white);
  }
  .brand__name {
    font-family: "Montserrat", sans-serif;
    font-weight: 600;
    font-size: 46px;
    letter-spacing: 0.5px;
    color: var(--white);
  }
  .front-details {
    position: absolute;
    left: 0;
    right: 0;
    top: 252px;
    font-family: "Questrial", sans-serif;
    font-size: 17px;
    line-height: 27px;
  }
  .front-details__tagline {
    font-family: "Montserrat", sans-serif;
    font-weight: 700;
    font-size: 16px;
  }

  /* Back */
  .services {
    position: absolute;
    left: 0;
    width: 496px;
    top: 54px;
    font-family: "Montserrat", sans-serif;
    font-weight: 500;
    font-size: 15.5px;
    line-height: 27px;
  }
  .services ul { list-style: none; }
  .contact {
    position: absolute;
    left: 0;
    width: 496px;
    top: 218px;
    font-family: "Questrial", sans-serif;
  }
  .contact__name {
    font-family: "Montserrat", sans-serif;
    font-weight: 700;
    font-size: 23px;
    line-height: 34px;
  }
  .contact__phone {
    font-size: 23px;
    line-height: 36px;
  }
  .contact__email {
    font-size: 25px;
    line-height: 36px;
  }
  .corner-dot {
    position: absolute;
    top: 34px;
    right: 52px;
    width: 16px;
    height: 16px;
    border-radius: 50%;
    background: var(--white);
  }
</style>
</head>
<body>
<main class="canvas">
  <section class="card card--front">
    <div class="brand">
      <span class="brand__dot"></span>
      <span class="brand__name">Bug Begone Bay</span>
    </div>
    <div class="front-details">
      <p class="front-details__tagline">Pest control services</p>
      <p>(00) 1234 5678</p>
      <p>hello@bugbegonebay.com.au</p>
    </div>
  </section>

  <section class="card card--back">
    <span class="corner-dot"></span>
    <div class="services">
      <p>Some information here about your services:</p>
      <ul>
        <li>- Termites</li>
        <li>- Rats and mice</li>
        <li>- Cockroaches</li>
        <li>- Silverfish</li>
      </ul>
    </div>
    <div class="contact">
      <p class="contact__name">Firstname Lastname</p>
      <p class="contact__phone">(00) 1234 5678</p>
      <p class="contact__email">hello@bugbegonebay.com.au</p>
    </div>
  </section>
</main>
</body>
</html>
```